One Page Magazine Ad for New Apartment in Calgary, AB Canada

We need a one page magazine ad for a new apartment community in Calgary, Alberta.

We pride ourselves in providing the highest level of customer service and the best amenities for our community.

COMMUNITY HIGHLIGHTS

- Brand new luxury apartment rental community in the exciting Calgary Beltline neighborhood
- 13 unique spacious floor plans fit for every lifestyle (1BR-1BATH, 2BR-1BATH & 2BR-2BATH)
- Professionally managed
- On-site staff during business hours to help you with any of your needs
- Pet-friendly community
- State of the art Fitness Facility
- 2 rooftop terraces outfitted with 8 Community Brimfield BBQs
- Great area for entertaining guests and a safe spot to take your dog out for some fresh air without leaving the building
- 2 resident lounges with multimedia suite, 60-inch TVs, Vexa Two, Silver Pin Arcade system, Poker table
- Great venues to host your next party, open 24/7 free to use and bookable by residents for free!
- Monthly resident events and parties hosted by the on-site staff
- Underground secured guest and resident parking available
- Electric Car Charging Stations
- Garbage & Recycling chutes on every floor
- Controlled Access/Building
- Gated Underground Parking Garage
- Adjacent to the Beltline neighborhood bike lane on 27th Avenue SW
- Elevators - Underground Secured Bike Storage and bike repair workstation
- On-site Maintenance
- Crate Keeper Package Management System
- Additional Storage Available
- Footsteps away from the local Fairmart Grocery and Fairmart Wine Store
- Minutes away from the new free leash dog park Wexley Park

APARTMENT AMENITIES

- Gourmet Kitchen with 4 piece Stainless Steel Appliances (Stove, Fridge, Microwave and Dishwasher)
- In suite dryer and washer
- Large Closets
- Patio/Balcony
- City and mountain views
- Ceramic Tile and Laminate Hardwood Flooring
- Quartz Counter-tops
- Roller Blinds for all Windows
- Walk-in Closets

For branding style, floor plans, amenities and photos please visit our website www.stayatthevorn.com

Target Market(s)

Young Adults and Recently Single Market

Industry/Entity Type

Real Estate

Font styles to use
Sans Serif

Colors
f37122

Requirements
Must have
• - Pictures of the community
• - Possibly use of a stock photo

```html
<!DOCTYPE html>
<html lang="en">
<head>
<meta charset="utf-8">
<title>The Vorn – Apartment Ad</title>
<link href="https://fonts.googleapis.com/css2?family=Antonio:wght@400;500&family=Questrial&display=swap" rel="stylesheet">
<style>
  :root {
    --orange: #f37122;
    --white: #ffffff;
    --grey-text: #6d6e71;
    --logo-grey: #7a7a7c;
    --logo-red: #ef4136;
    --shadow: rgba(70, 70, 70, 0.55);
  }
  html, body {
    margin: 0;
    padding: 0;
    overflow: hidden;
    background: #ffffff;
  }
  .ad {
    position: relative;
    width: 927px;
    height: 1200px;
    overflow: hidden;
    background: var(--white);
    font-family: "Questrial", sans-serif;
  }
  .brand {
    position: absolute;
    left: 0; top: 0;
    width: 462px; height: 302px;
    display: flex;
    flex-direction: column;
    align-items: center;
    justify-content: center;
    color: var(--logo-grey);
  }
  .brand-mark {
    width: 60px; height: 60px;
    background: var(--logo-red);
    margin-bottom: 26px;
  }
  .brand-name {
    text-align: center;
    font-size: 31px;
    letter-spacing: 7px;
    line-height: 36px;
    color: var(--logo-grey);
  }
  .photo {
    position: absolute;
    margin: 0;
  }
  .photo-building {
    left: 0; top: 302px; width: 462px; height: 406px;
    background: linear-gradient(180deg, #8fa6c0 0%, #c4ccd6 35%, #6b6863 60%, #8a3b33 78%, #3a3a3c 100%);
  }
  .photo-bedroom {
    left: 463px; top: 710px; width: 464px; height: 286px;
    background: linear-gradient(135deg, #d9dcdf 0%, #b9bcbf 45%, #4b4542 70%, #e6e4e1 100%);
  }
  .photo-living {
    left: 0; top: 998px; width: 308px; height: 202px;
    background: linear-gradient(160deg, #cfcac3 0%, #a39c92 55%, #1f8ea3 85%, #6d5a45 100%);
  }
  .photo-gym {
    left: 310px; top: 998px; width: 306px; height: 202px;
    background: linear-gradient(180deg, #2b2b2f 0%, #5a3b3e 40%, #3d3f45 75%, #1c1c1f 100%);
  }
  .photo-kitchen {
    left: 618px; top: 998px; width: 309px; height: 202px;
    background: linear-gradient(150deg, #e4e2de 0%, #c9c7c2 50%, #6f6d6a 80%, #a8a6a2 100%);
  }
  .highlights {
    position: absolute;
    left: 463px; top: 0;
    width: 464px; height: 708px;
    background: var(--orange);
    color: var(--white);
    box-sizing: border-box;
    padding: 48px 36px 0 26px;
  }
  .section-title {
    font-family: "Antonio", sans-serif;
    font-weight: 400;
    margin: 0;
    line-height: 1;
    letter-spacing: 0.5px;
  }
  .highlights .section-title {
    font-size: 55px;
    color: var(--white);
    text-shadow: 2px 2px 0 var(--shadow);
    padding-bottom: 14px;
    border-bottom: 1px solid rgba(255,255,255,0.8);
  }
  .highlight-columns {
    display: flex;
    gap: 22px;
    margin-top: 20px;
  }
  .feature-list {
    list-style: none;
    margin: 0;
    padding: 0;
    font-size: 12.4px;
    line-height: 15.3px;
  }
  .feature-list li {
    position: relative;
    padding-left: 14px;
    margin-bottom: 6.5px;
  }
  .feature-list li::before {
    content: "•";
    position: absolute;
    left: 1px; top: 0;
    font-size: 10px;
  }
  .highlight-columns .feature-list { width: 188px; }
  .amenities {
    position: absolute;
    left: 33px; top: 722px;
    width: 380px;
    color: var(--grey-text);
  }
  .amenities .section-title {
    font-size: 51px;
    color: var(--orange);
    text-shadow: 2px 2px 0 rgba(90,90,90,0.45);
    padding-bottom: 8px;
    border-bottom: 1px solid var(--orange);
  }
  .amenity-columns {
    display: flex;
    gap: 22px;
    margin-top: 12px;
    padding-bottom: 14px;
    border-bottom: 1px solid var(--orange);
  }
  .amenity-columns .feature-list { font-size: 12.6px; color: #4d4d4f; }
  .amenity-columns .feature-list:first-child { width: 178px; }
  .amenity-columns .feature-list:last-child { width: 180px; }
  .contact {
    margin-top: 10px;
    font-size: 13px;
    letter-spacing: 1.4px;
    line-height: 19px;
    color: var(--grey-text);
  }
  .contact p { margin: 0; }
</style>
</head>
<body>
<main class="ad">
  <header class="brand">
    <div class="brand-mark"></div>
    <div class="brand-name">THE<br>VORN</div>
  </header>

  <figure class="photo photo-building" role="img" aria-label="Exterior photo of the apartment tower at a street corner under a cloudy sky"></figure>

  <section class="highlights">
    <h2 class="section-title">COMMUNITY HIGHLIGHTS</h2>
    <div class="highlight-columns">
      <ul class="feature-list">
        <li>Brand new luxury apartment rental community in the exciting Calgary Beltline neighborhood</li>
        <li>13 unique spacious floor plans fit for every lifestyle (1BR-1BATH, 2BR-1BATH &amp; 2BR-2BATH)</li>
        <li>Professionally managed</li>
        <li>On-site staff during business hours to help you with any of your needs</li>
        <li>Pet-friendly community</li>
        <li>State of the art Fitness Facility</li>
        <li>2 rooftop terraces outfitted with 8 Community Brimfield BBQs</li>
        <li>Great area for entertaining guests and a safe spot to take your dog out for some fresh air without leaving the building</li>
        <li>2 resident lounges with multimedia suite, 60-inch TVs, Vexa Two, Silver Pin Arcade system, Poker table</li>
        <li>Great venues to host your next party, open 24/7 free to use and bookable by residents for free!</li>
      </ul>
      <ul class="feature-list">
        <li>Monthly resident events and parties hosted by the on-site staff</li>
        <li>Underground secured guest and resident parking available</li>
        <li>Electric Car Charging Stations</li>
        <li>Garbage &amp; Recycling chutes on every floor</li>
        <li>Controlled Access/Building</li>
        <li>Gated Underground Parking Garage</li>
        <li>Adjacent to the Beltline neighborhood bike lane on 27th Avenue SW</li>
        <li>Elevators - Underground Secured Bike Storage and bike repair workstation</li>
        <li>On-site Maintenance</li>
        <li>Crate Keeper Package Management System</li>
        <li>Additional Storage Available</li>
        <li>Footsteps away from the local Fairmart Grocery and Fairmart Wine Store</li>
        <li>Minutes away from the new free leash dog park Wexley Park</li>
      </ul>
    </div>
  </section>

  <section class="amenities">
    <h2 class="section-title">APARTMENT AMENITIES</h2>
    <div class="amenity-columns">
      <ul class="feature-list">
        <li>Gourmet Kitchen with 4 piece Stainless Steel Appliances (Stove, Fridge, Microwave and Dishwasher)</li>
        <li>In suite dryer and washer</li>
        <li>Large Closets</li>
        <li>Patio/Balcony</li>
      </ul>
      <ul class="feature-list">
        <li>City and mountain views</li>
        <li>Ceramic Tile and Laminate Hardwood Flooring</li>
        <li>Quartz Counter-tops</li>
        <li>Roller Blinds for all Windows</li>
        <li>Walk-in Closets</li>
      </ul>
    </div>
    <div class="contact">
      <p>4810 - 9TH AVENUE SW | CALGARY, AB T2R 1K4</p>
      <p>403.555.0142 | STAYATTHEVORN.COM</p>
    </div>
  </section>

  <figure class="photo photo-bedroom" role="img" aria-label="Bright bedroom with a large bed, fur throw, patterned pillows and a green armchair by the window"></figure>
  <figure class="photo photo-living" role="img" aria-label="Living room with a teal sofa, wooden coffee table and large windows"></figure>
  <figure class="photo photo-gym" role="img" aria-label="Fitness facility with treadmills, bikes and exercise machines"></figure>
  <figure class="photo photo-kitchen" role="img" aria-label="Modern kitchen with white cabinets, stainless steel appliances and quartz counters"></figure>
</main>
</body>
</html>
```